Book Cover - Life Lessons Book

I have written a book for my sons who are graduating high school and college. Working title is "Chart Your Compass.....38 Lessons Learned at Home" I am looking for the book to appeal to young adults and parents who would want to give this book to them. It is a 125 page book that will be hardback and paperback - probably 5x8 or 6x9.
Updates

Reason: Altered some of the design elements based on the first submissions received. Would really like to have designs by Monday, May 15, 2016 but could not force a 2 day extension.

Target Market(s)

Young adults -- graduates, 20-3- year olds. And, parents would would give a book to their kids

Industry/Entity Type

Book Publisher

Font styles to use
Serif

Requirements
Must have
• Great design. It is a book cover so needs to catch the attention.
Nice to have
• I am open to more animated/playful/modern look or a more traditional look. Just would like to appeal to young adults and parents.
Should not have
• Anything in poor taste

```html
<!DOCTYPE html>
<html lang="en">
<head>
<meta charset="utf-8">
<title>Chart Your Compass – Book Cover</title>
<link rel="stylesheet" href="https://fonts.googleapis.com/css2?family=Tinos:ital,wght@0,700;1,700&family=Varela+Round&display=swap">
<style>
  :root {
    --blue-deep: #2a1b6e;
    --blue-mid: #1556b0;
    --blue-light: #0094df;
    --grey-light: #b2b2b2;
    --grey-dark: #7c7c7c;
    --yellow: #f8c200;
    --orange: #e67a17;
    --ink: #1c1a1a;
    --white: #ffffff;
  }
  html, body {
    margin: 0;
    padding: 0;
    width: 800px;
    height: 1200px;
    overflow: hidden;
    background: var(--blue-mid);
  }
  .cover {
    position: relative;
    width: 800px;
    height: 1200px;
    overflow: hidden;
  }
  .cover-art {
    position: absolute;
    inset: 0;
    width: 800px;
    height: 1200px;
  }
  .title {
    position: absolute;
    left: 0;
    top: 0;
    width: 800px;
    margin: 0;
    text-align: center;
    font-family: "Tinos", "Times New Roman", serif;
    font-weight: 700;
    color: var(--white);
    text-shadow: 4px 4px 0 var(--ink), -1px -1px 0 var(--ink), 1px -1px 0 var(--ink), -1px 1px 0 var(--ink);
    line-height: 1;
  }
  .title-line { position: absolute; left: 0; width: 800px; display: block; }
  .title-first { top: 418px; font-size: 148px; }
  .title-middle { top: 568px; font-size: 96px; font-style: italic; }
  .title-last { top: 662px; font-size: 112px; }
  .lesson-count {
    position: absolute;
    left: 530px;
    top: 893px;
    width: 132px;
    height: 102px;
    background: var(--ink);
    color: var(--white);
    font-family: "Varela Round", "Arial Rounded MT Bold", sans-serif;
    font-size: 96px;
    line-height: 102px;
    text-align: center;
  }
  .subtitle {
    position: absolute;
    left: 394px;
    top: 1000px;
    width: 400px;
    margin: 0;
    text-align: center;
    font-family: "Tinos", "Times New Roman", serif;
    font-weight: 700;
    font-size: 44px;
    line-height: 58px;
    color: var(--ink);
  }
</style>
</head>
<body>
<main class="cover">
  <svg class="cover-art" viewBox="0 0 800 1200" xmlns="http://www.w3.org/2000/svg">
    <defs>
      <linearGradient id="bg-blue" x1="0" y1="0" x2="1" y2="1">
        <stop offset="0" stop-color="#1260b8"/>
        <stop offset="0.55" stop-color="#1a4fa8"/>
        <stop offset="1" stop-color="#2a1a6a"/>
      </linearGradient>
      <linearGradient id="bg-grey" x1="0" y1="0" x2="1" y2="0.4">
        <stop offset="0" stop-color="#b2b2b2"/>
        <stop offset="1" stop-color="#7c7c7c"/>
      </linearGradient>
      <linearGradient id="target-tones" x1="0" y1="0" x2="1" y2="1">
        <stop offset="0" stop-color="#e67a17"/>
        <stop offset="1" stop-color="#f0a020"/>
      </linearGradient>
    </defs>
    <rect class="backdrop" width="800" height="1200" fill="url(#bg-blue)"/>
    <path class="sky-arc" d="M0,0 L640,0 C660,240 520,470 330,555 C220,590 90,580 0,556 Z" fill="#0094df"/>
    <path class="grey-band" d="M0,837 C140,930 290,992 440,1000 L440,1200 L0,1200 Z" fill="url(#bg-grey)"/>
    <path class="yellow-band" d="M800,798 C620,828 480,915 410,1000 C340,1085 295,1145 262,1200 L800,1200 Z" fill="#f8c200"/>
    <circle class="target-art" cx="224" cy="224" r="181" fill="url(#target-tones)" role="img" aria-label="Illustration of an archery target with a silver arrow striking the bullseye"/>
  </svg>

  <h1 class="title">
    <span class="title-line title-first">Chart</span>
    <span class="title-line title-middle">Your</span>
    <span class="title-line title-last">Compass..</span>
  </h1>

  <div class="lesson-count">38</div>
  <p class="subtitle">Lessons Learned<br>at Home</p>
</main>
</body>
</html>
```